High end personal training flyer design

I want a flyer designed to be delivered to people's houses to interest them in high end (and, therefore, not cheap) personal training services.

Don't want standard pictures of people exercising, before and afters, etc. More something that will appeal to that more affluent market.

Flexible on size of flyer, but please make sure it is a standard size that I can get printed easily. Would like it not to look like a normal flyer you get through the letterbox, so if any particular sizes, shapes, etc are known to do that, then that would be a good start.

Text on flyer to be as follows:

Is this you:

Live in East Cheshire
Male, aged 30-50
A father
Cash rich, time poor
Find handling high pressure at work comfortable
But have a short fuse out of work – with the wife, kids, life in general, etc
Not happy with the way your body looks and feels
Know exactly what you should do to sort that, but struggling to actually do it for various reasons
Turned off by the standard menu of options for addressing that – gyms, slimming clubs, diets, etc

If so, you may be interested in what I do.

Some would call it Personal Training. Some would call it Coaching. I’m not interested in giving what I do labels.

What I am interested in is providing the best possible service (and results) for my clients – whatever that entails.

I work closely with one or two clients at a time to make sure they get exactly what they need.

If you would like to find out more about this, I usually meet for a coffee and a chat. To see if we both think our working together is a good idea.

No squeeze pages, no countdowns, mailing lists or false scarcity.

No plastering this flyer with ‘Before and afters’ – they are ten a penny and my clients don’t want to have pictures of them in their underwear spread around the local area.

Just give me a call and we’ll go from there.

My number is 07912645320.

Tim

Industry/Entity Type

Training

Requirements
Should not have
• Generic before and after or exercise type pictures

```html
<!DOCTYPE html>
<html lang="en">
<head>
<meta charset="utf-8">
<title>Personal Training Flyer</title>
<link rel="stylesheet" href="https://fonts.googleapis.com/css2?family=Oswald:wght@600;700&family=Source+Sans+3:wght@400;600&family=Open+Sans:wght@300&display=swap">
<style>
  :root {
    --backdrop: #764d2b;
    --red: #e31e26;
    --red-deep: #c1222f;
    --green: #8cc63f;
    --green-lime: #c6d92a;
    --green-text: #3aaa4a;
    --ink: #1f1f1f;
    --slate: #444444;
    --soft-grey: #e8e8e8;
    --white: #ffffff;
  }
  * { margin: 0; padding: 0; box-sizing: border-box; }
  html, body { width: 965px; height: 1200px; overflow: hidden; background: var(--backdrop); }
  .flyer {
    position: absolute; left: 90px; top: 100px; width: 784px; height: 1006px;
    background: var(--white); overflow: hidden;
    box-shadow: 4px 5px 8px rgba(0,0,0,.45);
    font-family: "Source Sans 3", sans-serif; color: var(--ink);
  }
  .shapes { position: absolute; inset: 0; }
  .abs { position: absolute; white-space: nowrap; }
  .headline {
    font-family: "Oswald", sans-serif; font-weight: 700; color: var(--white);
    font-size: 96px; line-height: 1; left: 44px; top: 36px; letter-spacing: 1px;
    text-shadow: 2px 3px 4px rgba(0,0,0,.35);
  }
  .location {
    font-family: "Oswald", sans-serif; font-weight: 700; color: var(--soft-grey);
    font-size: 46px; line-height: 1; left: 45px; top: 134px; letter-spacing: 1px;
    text-shadow: 1px 2px 3px rgba(0,0,0,.3);
  }
  .profile {
    font-family: "Open Sans", sans-serif; font-weight: 300; color: #555;
    font-size: 34px; line-height: 38px; text-align: center;
    left: 520px; top: 88px; width: 200px;
  }
  .intro { left: 39px; top: 290px; font-size: 20px; font-weight: 600; color: var(--green-text); }
  .offer { position: absolute; left: 40px; top: 331px; width: 356px; list-style: none; }
  .offer li {
    position: relative; padding-left: 18px; font-size: 12px; line-height: 15.5px;
    text-align: justify; margin-bottom: 8.5px;
  }
  .offer li.narrow { width: 300px; }
  .offer li.narrower { width: 240px; }
  .offer svg { position: absolute; left: 0; top: 2px; width: 12px; height: 12px; }
  .pain {
    right: 39px; top: 276px; text-align: right; font-size: 30px; line-height: 43.5px;
    font-weight: 600; color: var(--slate);
  }
  .stress {
    position: absolute; left: 508px; top: 432px; width: 238px;
    font-size: 17px; line-height: 25px; color: var(--slate); text-align: justify;
  }
  .badge-label {
    font-family: "Oswald", sans-serif; font-weight: 700; color: var(--ink);
    font-size: 44px; line-height: 46px; text-align: center;
    left: 66px; top: 845px; width: 200px;
  }
  .trainer-name {
    font-family: "Oswald", sans-serif; font-weight: 700; color: var(--white);
    font-size: 52px; line-height: 1; right: 42px; top: 818px;
    text-shadow: 2px 2px 3px rgba(0,0,0,.35);
  }
  .phone {
    font-family: "Oswald", sans-serif; font-weight: 700; color: var(--white);
    font-size: 55px; line-height: 1; right: 42px; top: 868px;
    text-shadow: 2px 2px 3px rgba(0,0,0,.35);
  }
  .call-to-action { right: 45px; top: 945px; font-size: 24px; color: var(--white); }
</style>
</head>
<body>
<main class="flyer">
  <svg class="shapes" viewBox="0 0 784 1006" width="784" height="1006" aria-hidden="true">
    <defs>
      <linearGradient id="redTop" x1="0" x2="1">
        <stop offset="0" stop-color="var(--red)"/><stop offset="1" stop-color="var(--red-deep)"/>
      </linearGradient>
      <linearGradient id="redBottom" x1="0" x2="1">
        <stop offset="0" stop-color="var(--red-deep)"/><stop offset="1" stop-color="var(--red)"/>
      </linearGradient>
      <radialGradient id="silver" cx=".62" cy=".35" r=".75">
        <stop offset="0" stop-color="#ffffff"/><stop offset=".45" stop-color="#e4e4e4"/><stop offset="1" stop-color="#8c8c8c"/>
      </radialGradient>
      <linearGradient id="sand" x1="0" y1="0" x2="0" y2="1">
        <stop offset="0" stop-color="#ffffff" stop-opacity="0"/><stop offset=".3" stop-color="#e9e3db"/><stop offset="1" stop-color="#c9b8a4"/>
      </linearGradient>
    </defs>

    <g role="img" aria-label="Photo of a smiling man doing push-ups on a sandy beach">
      <rect x="0" y="540" width="784" height="400" fill="url(#sand)"/>
      <ellipse cx="420" cy="760" rx="330" ry="140" fill="#d8c7b6" opacity=".55"/>
    </g>

    <path d="M0 0H784V256C700 206 620 190 520 202C380 222 200 282 0 268Z" fill="var(--green)"/>
    <path d="M0 0H784V228C700 182 620 168 520 182C380 202 200 260 0 238Z" fill="url(#redTop)"/>

    <circle cx="620" cy="150" r="104" fill="var(--green)"/>
    <circle cx="620" cy="150" r="98" fill="var(--green-lime)"/>
    <circle cx="620" cy="150" r="94" fill="#2a2a2a"/>
    <circle cx="620" cy="150" r="90" fill="url(#silver)"/>

    <path d="M784 694C600 838 300 900 0 910V1006H784Z" fill="#333"/>
    <path d="M784 703C600 848 300 906 0 914V1006H784Z" fill="var(--green)"/>
    <path d="M784 766C600 870 300 920 0 928V1006H784Z" fill="url(#redBottom)"/>

    <ellipse cx="166" cy="892" rx="114" ry="98" fill="var(--green)"/>
    <ellipse cx="166" cy="892" rx="106" ry="91" fill="var(--green-lime)"/>
    <ellipse cx="166" cy="892" rx="102" ry="87" fill="#2a2a2a"/>
    <ellipse cx="166" cy="892" rx="99" ry="84" fill="var(--green)"/>
  </svg>

  <h1 class="abs headline">IS THIS YOU</h1>
  <p class="abs location">LIVE IN EAST CHESHIRE</p>
  <p class="abs profile">A father,<br>Cash rich,<br>time poor</p>

  <h2 class="abs intro">If so, you may be interested in what I do</h2>
  <ul class="offer">
    <li><svg viewBox="0 0 12 12"><circle cx="6" cy="6" r="5.5" fill="#ddd"/><path d="M3 6l2.2 2.5L10 1.5" stroke="#222" stroke-width="1.6" fill="none"/></svg>Some would call it Personal Training. Some would call it Coaching. I’m not interested in giving what I do labels.</li>
    <li><svg viewBox="0 0 12 12"><circle cx="6" cy="6" r="5.5" fill="#ddd"/><path d="M3 6l2.2 2.5L10 1.5" stroke="#222" stroke-width="1.6" fill="none"/></svg>What I am interested in is providing the best possible service (and results) for my clients – whatever that entails.</li>
    <li><svg viewBox="0 0 12 12"><circle cx="6" cy="6" r="5.5" fill="#ddd"/><path d="M3 6l2.2 2.5L10 1.5" stroke="#222" stroke-width="1.6" fill="none"/></svg>I work closely with one or two clients at a time to make sure they get exactly what they need.</li>
    <li class="narrow"><svg viewBox="0 0 12 12"><circle cx="6" cy="6" r="5.5" fill="#ddd"/><path d="M3 6l2.2 2.5L10 1.5" stroke="#222" stroke-width="1.6" fill="none"/></svg>If you would like to find out more about this, I usually meet for a coffee and a chat. To see if we both think our working together is a good idea.</li>
    <li class="narrower"><svg viewBox="0 0 12 12"><circle cx="6" cy="6" r="5.5" fill="#ddd"/><path d="M3 6l2.2 2.5L10 1.5" stroke="#222" stroke-width="1.6" fill="none"/></svg>No squeeze pages, no countdowns, mailing lists or false scarcity.</li>
  </ul>

  <p class="abs pain">Not happy with<br>the way your body<br>looks and feels</p>
  <p class="stress">Find handling high pressure at work comfortable. But have a short fuse out of work – with the wife, kids,life in general, etc</p>

  <p class="abs badge-label">PERSONAL<br>TRAINING</p>
  <p class="abs trainer-name">TIM</p>
  <p class="abs phone">07912645320</p>
  <p class="abs call-to-action">Just give me a call and we’ll go from there</p>
</main>
</body>
</html>
```